I need a DVD cover for a training package contained on a disc. There are four modules within the resource so I need these to be visible on the cover. They are:
Cultural Competence Healthcare Provision
Provision of Care to CALD Women having Babies in Australia
Cultural Considerations in Aged Care Provision
Cultural Competence in Mental Health

I have attached a cd cover with an image of a waratah. This is Bellmore Ridge Valley Health's logo so needs to appear on the front cover also.
The smaller logo with the waratah also needs to be on the front cover. Please note these are the only copies I could obtain so if the quality is too poor you may need to reproduce.

The following should appear on the back cover:
‘Pathways to Inclusive Patient Support’ is a collaborative achievement of the Multicultural Health Liaison Officers in Acute Care, Obstetrics, Aged Care and Mental Health under the guidance of the Director, Multicultural Health Service in Bellmore Ridge Valley Local Health District. Staff members from the specialist teams and community members graciously contributed to the production of podcasts and video clips.
Photography, video clips and technical support was provided by Daniel Follett - E-learning Developer and Designer - Lumen Tutors.
This project was coordinated by Colleen Bastow, Multicultural Health Liaison Officer (Acute Care, Lower Brindlewood Coastal Hospital Network).

```html
<!DOCTYPE html>
<html lang="en">
<head>
<meta charset="utf-8">
<title>Pathways to Inclusive Patient Support – DVD Cover</title>
<link rel="stylesheet" href="https://fonts.googleapis.com/css2?family=Tinos:wght@700&family=Arimo:wght@400;600&display=swap">
<style>
  :root {
    --cover-blue: #0b4f9f;
    --cover-blue-deep: #0a4694;
    --front-light: #4c97d6;
    --front-pale: #9fd0f2;
    --band-blue: rgba(20, 96, 180, 0.82);
    --module-band: rgba(110, 170, 225, 0.55);
    --white: #ffffff;
    --logo-ink: #0b4f9f;
  }
  * { box-sizing: border-box; margin: 0; padding: 0; }
  html, body { width: 1200px; height: 802px; overflow: hidden; background: #ffffff; }
  .cover {
    position: relative; width: 1200px; height: 802px;
    background: var(--cover-blue); overflow: hidden;
    font-family: "Tinos", "Times New Roman", serif; color: var(--white);
  }

  /* Back cover */
  .back { position: absolute; left: 0; top: 0; width: 585px; height: 802px; }
  .back__tiles { position: absolute; left: 31px; top: 66px; display: flex; gap: 8px; }
  .back__tile { width: 118px; height: 96px; background: var(--white); }
  .back__title { position: absolute; left: 31px; top: 230px; font-size: 24px; font-weight: 700; letter-spacing: 0.2px; }
  .back__body { position: absolute; left: 31px; top: 292px; width: 520px; font-size: 14.4px; font-weight: 700; line-height: 18px; }
  .back__body p + p { margin-top: 18px; }

  /* Logo bars */
  .logo-bar {
    position: absolute; height: 46px; background: var(--white);
    display: flex; align-items: center; gap: 10px; padding-left: 18px;
  }
  .logo-bar--back { left: 258px; top: 668px; width: 325px; }
  .logo-bar--front { left: 860px; top: 668px; width: 340px; }
  .logo-mark { width: 22px; height: 22px; background: var(--logo-ink); flex: none; }
  .logo-name { font-family: "Arimo", Arial, sans-serif; font-weight: 600; font-size: 14px; color: var(--logo-ink); }

  /* Spine */
  .spine { position: absolute; left: 585px; top: 0; width: 34px; height: 802px; background: var(--cover-blue-deep); }
  .spine__title {
    position: absolute; left: 4px; top: 70px; width: 26px; height: 410px;
    writing-mode: vertical-rl; font-size: 21px; font-weight: 700; white-space: nowrap;
  }
  .spine__logo {
    position: absolute; left: 6px; top: 515px; width: 26px; height: 287px; background: var(--white);
    writing-mode: vertical-rl; display: flex; align-items: center; gap: 6px; padding-top: 6px;
  }
  .spine__logo .logo-mark { width: 12px; height: 12px; }
  .spine__logo .logo-name { font-size: 9px; }

  /* Front cover */
  .front {
    position: absolute; left: 619px; top: 12px; width: 581px; height: 790px;
    background: linear-gradient(180deg, var(--front-light) 0%, #2f7cc6 30%, #5aa6de 60%, var(--front-pale) 100%);
  }
  .front__photos { position: absolute; left: 16px; top: 60px; display: flex; gap: 9px; }
  .front__photo { height: 116px; }
  .front__photo--family { width: 143px; background: linear-gradient(135deg, #7a5236, #c9a07a); }
  .front__photo--newborn { width: 123px; background: linear-gradient(135deg, #f2ece8, #5b3a2a); }
  .front__photo--aged { width: 124px; background: linear-gradient(135deg, #d6e2ee, #6b86b8); }
  .front__photo--senior { width: 125px; background: linear-gradient(135deg, #e9e1d6, #7fa3cf); }
  .front__title-band { position: absolute; left: 0; top: 196px; width: 100%; height: 186px; background: var(--band-blue); }
  .front__title { position: absolute; left: 14px; top: 20px; font-size: 40px; font-weight: 700; line-height: 55px; letter-spacing: 0.5px; }
  .front__modules { position: absolute; left: 0; top: 393px; width: 100%; height: 102px; background: var(--module-band); padding: 7px 0 0 11px; }
  .front__modules li { list-style: none; font-size: 18.5px; font-weight: 700; line-height: 24px; white-space: nowrap; }
  .front__artwork {
    position: absolute; left: 0; top: 495px; width: 100%; height: 295px;
    background: radial-gradient(ellipse at 35% 45%, #d7eefb 0%, #8cc5ec 40%, #3b88cf 100%);
  }
</style>
</head>
<body>
<div class="cover">

  <section class="back">
    <div class="back__tiles">
      <div class="back__tile"></div><div class="back__tile"></div>
      <div class="back__tile"></div><div class="back__tile"></div>
    </div>
    <h2 class="back__title">Pathways to Inclusive Patient Support</h2>
    <div class="back__body">
      <p>is a collaborative achievement of the Multicultural Health Liaison Officers in Acute Care, Obstetrics, Aged Care and Mental Health under the guidance of the Director, Multicultural Health Service in Bellmore Ridge Valley Local Health District. Staff members from the specialist teams and community members graciously contributed to the production of podcasts and video clips.</p>
      <p>Photography, video clips and technical support was provided by Daniel Follett - E-learning Developer and Designer - Lumen Tutors.<br>This project was coordinated by Colleen Bastow, Multicultural Health Liaison Officer (Acute Care, Lower Brindlewood Coastal Hospital Network).</p>
    </div>
    <div class="logo-bar logo-bar--back">
      <span class="logo-mark"></span><span class="logo-name">Bellmore Ridge Valley Health</span>
    </div>
  </section>

  <section class="spine">
    <div class="spine__title">Pathways to Inclusive Patient Support</div>
    <div class="spine__logo">
      <span class="logo-mark"></span><span class="logo-name">Bellmore Ridge Valley Health</span>
    </div>
  </section>

  <section class="front">
    <div class="front__photos">
      <div class="front__photo front__photo--family" role="img" aria-label="Photo of a multigenerational family"></div>
      <div class="front__photo front__photo--newborn" role="img" aria-label="Photo of a mother holding a newborn baby"></div>
      <div class="front__photo front__photo--aged" role="img" aria-label="Photo of a nurse caring for an elderly woman"></div>
      <div class="front__photo front__photo--senior" role="img" aria-label="Photo of a smiling senior man"></div>
    </div>
    <div class="front__title-band">
      <h1 class="front__title">Pathways<br>to Inclusive<br>Patient Support</h1>
    </div>
    <ul class="front__modules">
      <li>Cultural Competence Healthcare Provision</li>
      <li>Provision of Care to CALD Women having Babies in Australia</li>
      <li>Cultural Considerations in Aged Care Provision</li>
      <li>Cultural Competence in Mental Health</li>
    </ul>
    <div class="front__artwork" role="img" aria-label="Illustration of a globe with a heartbeat line and medical cross"></div>
  </section>

  <div class="logo-bar logo-bar--front">
    <span class="logo-mark"></span><span class="logo-name">Bellmore Ridge Valley Health</span>
  </div>

</div>
</body>
</html>
```